Brightfield Chiropractic Business Cards

Business cards with new logo design. Will upload copy of current card. We like the layout, but we need a new logo. Family, husband holding up baby toward sky, mom and other child standing next to him. We will probably want to include a catch phrase with logo. TBD

```html
<!DOCTYPE html>
<html lang="en">
<head>
<meta charset="utf-8">
<title>Brightfield Chiropractic Business Cards</title>
<link href="https://fonts.googleapis.com/css2?family=Poppins:wght@400;500;600;800&display=swap" rel="stylesheet">
<style>
  :root {
    --stage: #2b2b2b;
    --card-white: #ffffff;
    --card-black: #0b0b0b;
    --ink: #111111;
    --red: #e3201b;
    --paper: #f4f4f4;
    --mist: #e6e6e6;
    --haze: #cfcfcf;
  }
  html, body {
    margin: 0;
    width: 1200px;
    height: 1108px;
    overflow: hidden;
    background: var(--stage);
    font-family: "Poppins", sans-serif;
  }
  .sheet {
    width: 1200px;
    height: 1108px;
    display: flex;
    justify-content: center;
    align-items: center;
    gap: 70px;
  }
  .card {
    width: 440px;
    height: 770px;
    border-radius: 18px;
    box-sizing: border-box;
    padding: 34px 34px 40px;
    display: flex;
    flex-direction: column;
    align-items: center;
  }
  .card--front { background: var(--card-white); color: var(--ink); }
  .card--back { background: var(--card-black); color: #fff; }

  .logo-art {
    width: 372px;
    height: 372px;
    border-radius: 18px;
    background: radial-gradient(circle at 50% 50%, var(--paper) 0%, var(--mist) 60%, var(--haze) 100%);
  }
  .brand {
    margin-top: 30px;
    font-weight: 800;
    font-size: 44px;
    line-height: 1.05;
    text-transform: uppercase;
    text-align: center;
    letter-spacing: 1px;
  }
  .card--front .brand { color: var(--ink); }
  .card--back .brand { color: var(--red); margin-top: 34px; }

  .doctor {
    margin-top: 26px;
    font-weight: 600;
    font-size: 24px;
  }
  .role {
    color: var(--red);
    font-size: 20px;
    margin-top: 2px;
  }
  .phone {
    margin-top: 18px;
    font-weight: 600;
    font-size: 27px;
  }
  .web {
    font-size: 19px;
    margin-top: 4px;
  }

  .map-art {
    width: 372px;
    height: 372px;
    border-radius: 10px;
    background: var(--paper);
  }
  .address {
    margin-top: 28px;
    text-align: center;
    font-size: 19px;
    line-height: 1.45;
  }
  .lines {
    margin-top: 18px;
    text-align: center;
    font-size: 19px;
    line-height: 1.45;
  }
</style>
</head>
<body>
<main class="sheet">
  <section class="card card--front">
    <div class="logo-art" role="img" aria-label="Logo artwork area: family scene with a father lifting a baby toward the sky"></div>
    <div class="brand">Brightfield<br>Chiropractic</div>
    <div class="doctor">Dr. Daniel R. Ostrander</div>
    <div class="role">Chiropractic Physician</div>
    <div class="phone">555-014-7786</div>
    <div class="web">www.Ostranderchiro.com</div>
  </section>

  <section class="card card--back">
    <div class="map-art" role="img" aria-label="Street map showing the clinic location between nearby avenues, a market and a restaurant"></div>
    <div class="brand">Brightfield<br>Chiropractic</div>
    <div class="address">2480 SE Willow Creek Center Dr.<br>Maple Grove, Oregon 97000</div>
    <div class="lines">555-014-7786<br>Fax: 555-014-7191</div>
  </section>
</main>
</body>
</html>
```